DOUBLE SIDED BROCHURE NEEDED TO PROMOTE DOCTOR

I need a double sided DL size (99mm x 210mm) brochure, promoting a doctor seeing patients in a new area.

I want something professional. I have included the relevant information. I would also like the Dr's picture somwhere in the brochure, with a professional background. I wish to print these tomorrow, so i will pick a winner within 14 hours of posting this ad.

I have included an example of a brochures design that I recently saw, and its definietly a good starting point.

Medical

```html
<!DOCTYPE html>
<html lang="en">
<head>
<meta charset="utf-8">
<title>Dr. Karim Haddad – DL Brochure</title>
<link href="https://fonts.googleapis.com/css2?family=Oswald:wght@500;600&family=Arimo:wght@400;700&family=Tinos&family=Open+Sans:wght@600;700&display=swap" rel="stylesheet">
<style>
:root{
  --backdrop:#e4e6e4;
  --cream:#fdfbf4;
  --yellow:#e9ac2a;
  --yellow-bright:#efc526;
  --orange:#d97a1e;
  --charcoal:#2e2f34;
  --black:#1c1c1c;
  --crimson:#8e1537;
  --ink:#2a2a2a;
  --grey-text:#444;
  --rule:#c9c6bd;
  --white:#ffffff;
}
*{margin:0;padding:0;box-sizing:border-box}
html,body{width:1200px;height:887px;overflow:hidden}
body{background:var(--backdrop);position:relative}
.panel{position:absolute;top:22px;width:397px;height:839px;background:var(--cream);overflow:hidden;box-shadow:0 4px 14px rgba(0,0,0,.18)}
.panel--front{left:155px}
.panel--back{left:636px}
.panel__shapes{position:absolute;inset:0;width:100%;height:100%}
.doctor-name{position:absolute;font-family:"Oswald",sans-serif;font-weight:600;letter-spacing:-.5px;line-height:1;white-space:nowrap}
.panel--front .doctor-name{left:98px;top:9px;font-size:29px;color:var(--black)}
.panel--back .doctor-name{left:162px;top:64px;font-size:32px;color:var(--white)}
.clinic-address{position:absolute;font-family:"Oswald",sans-serif;font-weight:500;font-variant:small-caps;font-size:15px;line-height:17px;letter-spacing:.2px;white-space:nowrap}
.panel--front .clinic-address{left:14px;top:115px;color:var(--white)}
.panel--back .clinic-address{left:77px;top:688px;color:var(--black)}
.pin{position:absolute;left:57px;top:691px;width:13px;height:18px}
.greeting{position:absolute;left:36px;top:512px;width:176px;height:26px;border-radius:13px;background:var(--charcoal);color:var(--white);font-family:"Arimo",sans-serif;font-size:21px;line-height:26px;padding-left:15px;white-space:nowrap}
.greeting b{font-weight:700}
.letter{position:absolute;left:49px;top:553px;width:305px;font-family:"Tinos",serif;font-size:14.5px;line-height:18.4px;color:var(--ink);text-align:justify}
.letter p{padding-bottom:6px;border-bottom:1px dotted var(--rule);margin-bottom:10px}
.letter p:first-child{position:relative}
.letter p:first-child::before{content:"";position:absolute;left:-20px;top:3px;width:10px;height:11px;background:var(--orange);clip-path:polygon(0 0,100% 50%,0 100%,35% 50%)}
.fax-note{position:absolute;left:17px;top:752px;font-family:"Open Sans",sans-serif;font-weight:700;font-size:12.5px;color:var(--black);white-space:nowrap}
.phone-band{position:absolute;left:17px;top:786px;display:flex;align-items:center;gap:12px;color:var(--white);font-family:"Open Sans",sans-serif;font-weight:700;font-size:19px;white-space:nowrap}
.phone-band svg{width:24px;height:24px}
.intro{position:absolute;font-family:"Arimo",sans-serif;font-weight:700;font-size:17.5px;line-height:18.6px;color:var(--crimson)}
.intro--specialty{left:35px;top:268px;width:300px}
.intro--general{left:42px;top:495px;white-space:nowrap}
.services{position:absolute;left:66px;list-style:none;font-family:"Arimo",sans-serif;font-size:14.5px;color:var(--grey-text)}
.services--specialty{top:362px}
.services--general{top:521px}
.services li{position:relative;padding-left:37px;line-height:22.8px;white-space:nowrap}
.services li span{display:inline-block;border-bottom:1px dotted var(--rule);min-width:268px;padding-right:4px;line-height:21.8px}
.services--general li span{min-width:156px}
.services li::before{content:"";position:absolute;left:0;top:6px;width:11px;height:11px;background:var(--black);clip-path:polygon(0 0,100% 50%,0 100%,35% 50%)}
.services li.orange::before{background:var(--orange)}
.services li::after{content:"";position:absolute;left:19px;top:9px;width:5px;height:5px;border-radius:50%;background:var(--grey-text)}
.services li.continued::before,.services li.continued::after{display:none}
</style>
</head>
<body>

<section class="panel panel--front">
  <svg class="panel__shapes" viewBox="0 0 496 1048" preserveAspectRatio="none" aria-hidden="true">
    <polygon points="0,0 392,0 300,60 0,22" fill="var(--yellow)"/>
    <polygon points="0,22 300,60 240,100 70,395 0,360" fill="var(--charcoal)"/>
    <polygon points="0,360 70,395 310,548 420,622 0,556" fill="var(--yellow)"/>
    <polygon points="0,556 420,622 0,590" fill="#d9d4c8" opacity=".35"/>
    <polygon points="310,548 496,496 420,622" fill="var(--orange)"/>
    <polygon points="420,622 496,496 496,965" fill="var(--yellow)"/>
    <polygon points="0,968 405,968 375,1015 0,1015" fill="var(--black)"/>
    <polygon points="330,1048 358,1010 496,1010 496,1048" fill="var(--yellow-bright)"/>
  </svg>
  <svg class="panel__shapes" viewBox="0 0 496 1048" preserveAspectRatio="none" role="img" aria-label="Portrait photo of the doctor in glasses, navy blazer and checked shirt">
    <defs>
      <linearGradient id="portrait-tone" x1="0" y1="0" x2="0" y2="1">
        <stop offset="0" stop-color="#8a8580"/>
        <stop offset=".45" stop-color="#b98c72"/>
        <stop offset="1" stop-color="#1f2535"/>
      </linearGradient>
    </defs>
    <polygon points="125,440 200,150 300,55 420,90 496,300 496,496 310,548" fill="url(#portrait-tone)"/>
  </svg>
  <div class="doctor-name">Dr. Karim Haddad</div>
  <div class="clinic-address">Coralbay Clinic:<br>48 Harbour View Road<br>Coralbay WA 6290.</div>
  <div class="greeting"><b>Dear</b> Doctors,</div>
  <div class="letter">
    <p>We are pleased to announce that Dr. Karim Haddad is now consulting in Coralbay, seeing public and private patients.</p>
    <p>Guaranteed appointment within two weeks, with patients having the option of surgery at Coralbay Health Campus, Westmere Hospital or St. Alder Private Westfield.</p>
  </div>
  <div class="fax-note">Please send all referrals by fax to (08) 6000 4821.</div>
  <div class="phone-band">
    <svg viewBox="0 0 24 24" aria-hidden="true"><circle cx="12" cy="12" r="11" fill="none" stroke="var(--white)" stroke-width="1.5"/><path d="M8 6.5c.6-.4 1.2-.2 1.5.3l1 1.8c.3.5.1 1-.3 1.3l-.8.5c.5 1.3 1.7 2.6 3 3.2l.5-.8c.3-.4.9-.6 1.3-.3l1.8 1c.5.3.7.9.3 1.5-.8 1.2-2 1.6-3.3 1-2.6-1.2-4.6-3.3-5.7-5.8-.5-1.3-.1-2.6.7-3.7z" fill="var(--white)"/></svg>
    Phone: 1300 000 482
  </div>
</section>

<section class="panel panel--back">
  <svg class="panel__shapes" viewBox="0 0 496 1048" preserveAspectRatio="none" aria-hidden="true">
    <polygon points="0,0 310,195 425,272 0,205" fill="var(--yellow)"/>
    <polygon points="0,0 496,0 496,145 310,195" fill="var(--black)"/>
    <polygon points="310,195 496,145 425,272" fill="var(--orange)"/>
    <polygon points="425,272 496,145 496,610" fill="var(--yellow)"/>
    <polygon points="0,968 408,968 378,1015 0,1015" fill="var(--black)"/>
    <polygon points="300,1048 330,1010 496,1010 496,1048" fill="var(--yellow-bright)"/>
  </svg>
  <div class="doctor-name">Dr. Karim Haddad</div>
  <div class="intro intro--specialty">Dr. Haddad is a highly trained specialised surgeon, in all areas of Endocrine, Breast and General Surgery. Including;</div>
  <ul class="services services--specialty">
    <li><span>Thyroid Surgery</span></li>
    <li class="orange"><span>Parathyroid surgery (including</span></li>
    <li class="continued"><span>minimally invasive parathyroidectomy)</span></li>
    <li><span>Breast Cancer</span></li>
    <li class="orange"><span>Benign breast lesions</span></li>
  </ul>
  <div class="intro intro--general">All areas of general surgery, such as;</div>
  <ul class="services services--general">
    <li><span>Gallbladder surgery</span></li>
    <li class="orange"><span>Hernia surgery</span></li>
    <li><span>Haemorrhoids</span></li>
    <li class="orange"><span>Carpal Tunnel</span></li>
    <li><span>Vasectomy etc etc…</span></li>
  </ul>
  <svg class="pin" viewBox="0 0 13 18" aria-hidden="true"><path d="M6.5 1C3.5 1 1.2 3.3 1.2 6.2c0 3.8 5.3 10.5 5.3 10.5s5.3-6.7 5.3-10.5C11.8 3.3 9.5 1 6.5 1z" fill="none" stroke="var(--orange)" stroke-width="1.6"/><circle cx="6.5" cy="6.2" r="2" fill="var(--orange)"/></svg>
  <div class="clinic-address">Coralbay Clinic:<br>48 Harbour View Road<br>Coralbay WA 6290.</div>
  <div class="fax-note">Please send all referrals by fax to (08) 6000 4821.</div>
  <div class="phone-band">
    <svg viewBox="0 0 24 24" aria-hidden="true"><circle cx="12" cy="12" r="11" fill="none" stroke="var(--white)" stroke-width="1.5"/><path d="M8 6.5c.6-.4 1.2-.2 1.5.3l1 1.8c.3.5.1 1-.3 1.3l-.8.5c.5 1.3 1.7 2.6 3 3.2l.5-.8c.3-.4.9-.6 1.3-.3l1.8 1c.5.3.7.9.3 1.5-.8 1.2-2 1.6-3.3 1-2.6-1.2-4.6-3.3-5.7-5.8-.5-1.3-.1-2.6.7-3.7z" fill="var(--white)"/></svg>
    Phone: 1300 000 482
  </div>
</section>

</body>
</html>
```